Apricot Variety Sheet - Meadowlark Orchard Co

We are needing a variety sheet that we can hand out that will describe the different apricot vatieties we have available. The attached document has the name of the variety along with a description that will need to be on the sheet. We are looking for a modern, appealing way to display this information on 1 page (if needed, it can be front and back)
Updates

Apologies for the delay; we are overwhelmed with the great design options and will be sorting through them all (across our contests) to pick a collective. Thank you for your patience.

Target Market(s)

Growers and consumers

Industry/Entity Type

Agriculture

Requirements
Must have
• Easy to read
• Natural color palettes to emphasize the agricultural nature
• Clearly show washington as the origin in the title or at the top
Nice to have
• incorporate Apricots in the design

```html
<!DOCTYPE html>
<html lang="en">
<head>
<meta charset="utf-8">
<title>Apricot Variety Sheet – Meadowlark Orchard Co</title>
<link href="https://fonts.googleapis.com/css2?family=Bebas+Neue&family=Montserrat:wght@400;700&display=swap" rel="stylesheet">
<style>
  :root{
    --stage:#595959;
    --paper:#faf9f5;
    --heading:#8a5a2b;
    --body:#3a3a3a;
    --dash:#f0c48a;
    --leaf:#bfe5a6;
    --honey:#f4c24c;
    --honey-pale:#fbe3a0;
    --peach:#f6c9a0;
    --brand:#2f6b3a;
  }
  *{box-sizing:border-box;margin:0;padding:0}
  html,body{width:1200px;height:922px;overflow:hidden;background:var(--stage)}
  .spread{position:relative;width:1200px;height:922px}
  .sheet{position:absolute;top:98px;width:560px;height:725px;background:var(--paper);overflow:hidden;box-shadow:0 6px 18px rgba(0,0,0,.35)}
  .sheet--front{left:20px}
  .sheet--back{left:620px}

  .wash{position:absolute}
  .wash--header{left:190px;top:0;width:370px;height:215px;background:radial-gradient(ellipse at 60% 40%,var(--honey) 0%,#f7d26f 55%,rgba(251,227,160,0) 78%)}
  .wash--peach{left:-40px;top:-20px;width:300px;height:290px;background:radial-gradient(ellipse at 50% 60%,var(--peach) 0%,rgba(246,201,160,.5) 45%,rgba(250,249,245,0) 75%)}
  .wash--corner{left:250px;top:0;width:310px;height:190px;background:radial-gradient(ellipse at 70% 30%,var(--honey-pale) 0%,rgba(251,227,160,.6) 45%,rgba(250,249,245,0) 75%)}
  .wash--foot{left:0;top:560px;width:260px;height:190px;background:radial-gradient(ellipse at 30% 70%,var(--honey-pale) 0%,rgba(250,249,245,0) 70%)}

  .sheet-title{position:absolute;left:28px;top:52px;font:400 47px/0.98 "Bebas Neue",sans-serif;color:#fff;letter-spacing:2px}
  .brand-title{position:absolute;right:28px;top:30px;text-align:right;color:#fff;font-family:"Bebas Neue",sans-serif;line-height:.95}
  .brand-title .line1{display:block;font-size:58px;letter-spacing:1px}
  .brand-title .line2{display:block;font-size:40px}
  .brand-title .origin{display:block;font-size:20px;letter-spacing:3px;margin-top:6px;color:var(--heading)}

  .variety{position:absolute;font:400 9px/1.38 "Montserrat",sans-serif;color:var(--body);text-align:justify}
  .variety h2{font:400 25px/1 "Bebas Neue",sans-serif;color:var(--heading);letter-spacing:.5px;margin-bottom:3px;text-align:left}
  .dash-lb{border-left:1px dashed var(--dash);border-bottom:1px dashed var(--dash);padding:0 0 10px 10px}
  .dash-rb{border-right:1px dashed var(--dash);border-bottom:1px dashed var(--dash);padding:0 10px 10px 0}

  .photo,.leaf{position:absolute}

  .partner{position:absolute;left:350px;top:660px;display:flex;align-items:center;gap:10px;background:#fff;padding:10px 14px;width:200px}
  .partner-dot{width:38px;height:38px;border-radius:50%;background:#d9543a;flex:none}
  .partner-name{font:700 13px/1.15 "Montserrat",sans-serif;color:var(--brand)}
</style>
</head>
<body>
<main class="spread">

  <section class="sheet sheet--front">
    <div class="wash wash--peach"></div>
    <div class="wash wash--header" role="img" aria-label="Watercolour outline map of Washington State"></div>
    <div class="wash wash--foot"></div>

    <h1 class="sheet-title">Apricot<br>Variety<br>Sheet</h1>
    <p class="brand-title"><span class="line1">Meadowlark</span><span class="line2">Orchard Co</span><span class="origin">Grown in Washington</span></p>

    <svg class="leaf" style="left:470px;top:140px" width="90" height="100" viewBox="0 0 90 110"><path d="M90,0 C40,10 10,50 25,95 C35,110 90,110 90,80Z" fill="var(--leaf)"/></svg>

    <svg class="photo" style="left:300px;top:195px" width="260" height="150" viewBox="0 0 260 170" preserveAspectRatio="none" role="img" aria-label="Photo of a halved apricot with its stone on a wooden board">
      <defs><linearGradient id="g-half" x1="0" y1="0" x2="1" y2="1"><stop offset="0" stop-color="#f7a640"/><stop offset=".6" stop-color="#f08a1f"/><stop offset="1" stop-color="#c98a5a"/></linearGradient></defs>
      <path d="M260,0 L260,60 C240,140 170,170 90,165 C50,162 20,150 0,135 C60,140 110,110 140,60 C170,15 215,0 260,0Z" fill="url(#g-half)"/>
    </svg>

    <article class="variety dash-lb" style="left:50px;top:240px;width:260px">
      <h2>Rival</h2>
      <p>Great flavor with a fine, firm texture distinguishes this large oval-shaped apricot. The skin is light orange with a red blush. The flesh is a lush deep orange color. Available early July- early August.</p>
    </article>

    <svg class="leaf" style="left:28px;top:345px" width="50" height="80" viewBox="0 0 50 80"><path d="M0,0 C35,10 50,45 30,80 C10,70 0,40 0,0Z" fill="var(--leaf)"/></svg>

    <svg class="photo" style="left:40px;top:340px" width="215" height="145" viewBox="0 0 215 175" preserveAspectRatio="none" role="img" aria-label="Photo of ripe apricots hanging on a branch">
      <defs><linearGradient id="g-branch" x1="0" y1="0" x2="1" y2="1"><stop offset="0" stop-color="#f5b067"/><stop offset=".5" stop-color="#ee8a42"/><stop offset="1" stop-color="#9cc47a"/></linearGradient></defs>
      <path d="M215,0 C215,90 170,175 80,175 C30,175 0,150 0,120 C0,85 40,75 90,75 C150,75 200,50 215,0Z" fill="url(#g-branch)"/>
    </svg>

    <article class="variety dash-rb" style="left:275px;top:348px;width:268px">
      <h2>Robada</h2>
      <p>This jumbo apricot has a delicious floral flavor with a firm texture. Bright orange, with a deep red blush over nearly half its surface. Available early June.</p>
    </article>

    <article class="variety dash-rb" style="left:275px;top:432px;width:272px">
      <h2>Perfection</h2>
      <p>This classic large oval apricot is deep orange with an oblong shape and firm texture. The flesh is a yellow/orange color that is very sweet and full of flavor. Available mid July - mid August.</p>
    </article>

    <svg class="leaf" style="left:485px;top:535px" width="75" height="105" viewBox="0 0 75 115"><path d="M40,0 C5,30 0,85 40,115 L75,115 L75,40 C65,20 55,8 40,0Z" fill="var(--leaf)"/></svg>

    <article class="variety dash-rb" style="left:50px;top:530px;width:405px">
      <h2>Patterson</h2>
      <p>This apricot has a well-balanced flavor and an excellent shelf life. This is perfect for canning or drying. It has streaked red over yellow skin, with a firm flesh. Available mid – late June.</p>
    </article>

    <article class="variety" style="left:60px;top:612px;width:215px">
      <h2>Tomcot</h2>
      <p>Tangy, sweet flavor with a firm texture. This oval apricot is light orange with a slight blush color. The flesh is a dark orange. Available late June – late July.</p>
    </article>

    <svg class="photo" style="left:280px;top:625px" width="280" height="100" viewBox="0 0 295 100" preserveAspectRatio="none" role="img" aria-label="Photo of a pile of dried apricots">
      <defs><linearGradient id="g-dried" x1="0" y1="0" x2="1" y2="1"><stop offset="0" stop-color="#f3a44a"/><stop offset=".6" stop-color="#e27a1c"/><stop offset="1" stop-color="#f4b860"/></linearGradient></defs>
      <path d="M295,0 L295,100 L0,100 C30,95 60,75 90,50 C140,10 210,-5 295,0Z" fill="url(#g-dried)"/>
    </svg>
  </section>

  <section class="sheet sheet--back">
    <div class="wash wash--corner"></div>

    <svg class="leaf" style="left:0;top:0" width="40" height="60" viewBox="0 0 40 60"><path d="M0,0 L25,0 C40,20 35,45 0,60Z" fill="var(--leaf)"/></svg>

    <svg class="photo" style="left:5px;top:10px" width="235" height="150" viewBox="0 0 235 150" role="img" aria-label="Photo of fresh apricots resting on leaves">
      <defs><linearGradient id="g-rest" x1="0" y1="0" x2="1" y2="1"><stop offset="0" stop-color="#7aa35a"/><stop offset=".35" stop-color="#f4a640"/><stop offset="1" stop-color="#f08a24"/></linearGradient></defs>
      <path d="M235,0 C225,90 170,150 100,150 C40,150 0,115 0,80 C0,45 40,30 100,30 C150,30 205,25 235,0Z" fill="url(#g-rest)"/>
    </svg>

    <article class="variety dash-lb" style="left:250px;top:50px;width:270px">
      <h2>Goldrich</h2>
      <p>This apricot is round with a bright orange skin color and a deep orange flesh. It has a mild, sweet flavor with a firm texture. Available early July – mid August.</p>
    </article>

    <article class="variety dash-rb" style="left:22px;top:190px;width:290px">
      <h2>Casselbrite</h2>
      <p>This medium sized apricot is golden orange with a slight red blush. It has a mild sweet-tart flavor that is good for eating out of hand. Available late June-early July.</p>
    </article>

    <article class="variety dash-rb" style="left:28px;top:292px;width:290px">
      <h2>Goldbar</h2>
      <p>Moderately juicy, this large oval-shaped apricot has a light yellow-orange with a reddish blush. The flesh is firm, meaty, and has a light orange color. Available late June – end of July.</p>
    </article>

    <article class="variety dash-rb" style="left:30px;top:392px;width:290px">
      <h2>Sweet Juillet</h2>
      <p>This special variety has a unique, sweet flavor with a juicy flesh. It is bright orange in color with a bright orange flesh. Available through July.</p>
    </article>

    <svg class="photo" style="left:315px;top:140px" width="245" height="320" viewBox="0 0 245 320" role="img" aria-label="Photo of a cluster of golden apricots on the tree">
      <defs><linearGradient id="g-tree" x1="0" y1="0" x2="1" y2="1"><stop offset="0" stop-color="#4f8a3a"/><stop offset=".4" stop-color="#f2b42a"/><stop offset=".8" stop-color="#f09a1c"/><stop offset="1" stop-color="#5f9a44"/></linearGradient></defs>
      <path d="M80,0 C70,40 0,90 0,170 C0,250 50,320 245,320 L245,40 C200,30 120,30 80,0Z" fill="url(#g-tree)"/>
    </svg>

    <svg class="leaf" style="left:470px;top:430px" width="90" height="75" viewBox="0 0 90 75"><path d="M90,0 C40,0 5,30 0,75 C50,70 85,45 90,0Z" fill="var(--leaf)"/></svg>

    <article class="variety dash-lb" style="left:292px;top:480px;width:250px">
      <h2>Tasty Rich</h2>
      <p>This early variety is light yellow-orange colored with a firm texture. Very juicy with an enticing flavor. Available through June.</p>
    </article>

    <article class="variety dash-lb" style="left:292px;top:560px;width:250px">
      <h2>Gold Strike</h2>
      <p>A larger apricot with light orange, blushed skin. Firm texture with a slight tart taste until fully ripened, then very sweet. Available mid June - mid July.</p>
    </article>

    <svg class="leaf" style="left:25px;top:470px" width="60" height="110" viewBox="0 0 60 110"><path d="M30,0 C0,30 0,80 40,110 C60,80 60,30 30,0Z" fill="var(--leaf)"/></svg>

    <svg class="photo" style="left:35px;top:490px" width="250" height="140" viewBox="0 0 250 140" role="img" aria-label="Photo of blushed apricots among green leaves">
      <defs><linearGradient id="g-blush" x1="0" y1="0" x2="1" y2="1"><stop offset="0" stop-color="#5f9a3e"/><stop offset=".45" stop-color="#f3a54a"/><stop offset="1" stop-color="#e9824a"/></linearGradient></defs>
      <path d="M0,30 C30,5 100,0 160,10 C210,20 240,50 250,140 C200,120 150,120 90,120 C30,120 0,90 0,30Z" fill="url(#g-blush)"/>
    </svg>

    <article class="variety" style="left:40px;top:650px;width:275px">
      <h2>Riland</h2>
      <p>Very aromatic and sweet, this apricot is orange with a red blush. It has a yellow-orange colored flesh and a round shape. Available mid-June to end of July.</p>
    </article>

    <div class="partner">
      <span class="partner-dot"></span>
      <span class="partner-name">Cascade Growers Council</span>
    </div>
  </section>

</main>
</body>
</html>
```